Business Card Design Project

I am opening a skin care studio called Glow Bloom by Marisa. I will be offering a wide range of unique and affordable skin services including facials, chemical peels, microdermabrasion treatments, body wraps, salt glows, all waxing and eye lash extensions. If the business cards depicts what I would like, this would lead to brochures, web design, signs, etc.
Updates

Project Deadline Extended
Reason: A request to extend deadline was requested. I will be more than happy to accommodate.

Industry/Entity Type

Business

Requirements
Nice to have
• facial features so prospective client clearly identifies what type of business this is. Not stuffy or boring "spa" looking graphics. I am focusing just on face, body, waxing, eyelashes. No massage or nails.

```html
<!DOCTYPE html>
<html lang="en">
<head>
<meta charset="utf-8">
<title>Glow Bloom by Marisa – Business Card</title>
<link rel="stylesheet" href="https://fonts.googleapis.com/css2?family=Didact+Gothic&family=Mrs+Saint+Delafield&display=swap">
<style>
  :root {
    --page-bg: #f1f1f1;
    --card-black: #1b1b1b;
    --card-black-edge: #2a2a2a;
    --card-white: #f6f5f3;
    --ink: #1c1c1c;
    --accent-pink: #e0529b;
    --logo-tone: #e58cc0;
    --wash-blue: #3f86c9;
    --wash-sky: #9fd0ea;
    --wash-violet: #8b7fc8;
    --wash-rose: #ef8fbf;
    --wash-magenta: #e0469a;
  }
  * { box-sizing: border-box; margin: 0; padding: 0; }
  html, body {
    width: 1200px;
    height: 1200px;
    overflow: hidden;
    background: var(--page-bg);
  }
  .sheet {
    position: relative;
    width: 1200px;
    height: 1200px;
  }
  .card {
    position: absolute;
    left: 210px;
    width: 780px;
    height: 446px;
    border-radius: 4px;
    overflow: hidden;
    box-shadow: 0 6px 22px rgba(0,0,0,0.14);
  }

  /* Front side */
  .card--front {
    top: 110px;
    background: linear-gradient(160deg, var(--card-black-edge), var(--card-black) 60%);
    display: flex;
    flex-direction: column;
    align-items: center;
    justify-content: center;
    font-family: "Didact Gothic", "Century Gothic", sans-serif;
    color: var(--logo-tone);
  }
  .brand-name {
    font-size: 62px;
    letter-spacing: 2px;
    line-height: 1;
    font-weight: 400;
  }
  .brand-byline {
    margin-top: 12px;
    font-size: 30px;
    letter-spacing: 1px;
    line-height: 1;
    font-weight: 400;
  }

  /* Back side */
  .card--back {
    top: 636px;
    background: var(--card-white);
    font-family: "Didact Gothic", "Century Gothic", sans-serif;
    color: var(--ink);
  }
  .portrait-wash {
    position: absolute;
    left: 0;
    top: 0;
    width: 430px;
    height: 100%;
    background:
      radial-gradient(ellipse 45% 30% at 40% 22%, var(--wash-blue), transparent 70%),
      radial-gradient(ellipse 40% 35% at 62% 55%, var(--wash-sky), transparent 75%),
      radial-gradient(ellipse 25% 45% at 10% 60%, var(--wash-magenta), transparent 70%),
      radial-gradient(ellipse 40% 30% at 50% 88%, var(--wash-violet), transparent 75%),
      radial-gradient(ellipse 30% 25% at 72% 40%, var(--wash-rose), transparent 75%),
      linear-gradient(90deg, #c9c3e6, #e7e2f1);
    -webkit-mask-image: linear-gradient(90deg, #000 55%, transparent 100%);
    mask-image: linear-gradient(90deg, #000 55%, transparent 100%);
  }
  .back-content {
    position: absolute;
    right: 30px;
    top: 30px;
    bottom: 28px;
    width: 540px;
    text-align: right;
  }
  .tagline {
    font-size: 21px;
    letter-spacing: 0.4px;
    line-height: 1.1;
  }
  .tagline__accent { color: var(--accent-pink); }
  .specialty {
    font-size: 14.5px;
    letter-spacing: 0.3px;
    margin-top: 4px;
  }
  .owner {
    margin-top: 58px;
    margin-right: 30px;
    font-family: "Mrs Saint Delafield", cursive;
    font-size: 64px;
    line-height: 1;
    font-weight: 400;
  }
  .owner-title {
    margin-top: 10px;
    margin-right: 96px;
    font-size: 15px;
    letter-spacing: 0.4px;
  }
  .contact {
    position: absolute;
    right: 0;
    bottom: 0;
    font-style: normal;
    font-size: 21px;
    line-height: 1.42;
  }
</style>
</head>
<body>
  <main class="sheet">
    <section class="card card--front" aria-label="Business card front">
      <h1 class="brand-name">GLOW BLOOM</h1>
      <p class="brand-byline">by marisa</p>
    </section>

    <section class="card card--back" aria-label="Business card back">
      <div class="portrait-wash" role="img" aria-label="Watercolor portrait of a woman's profile in blue, pink and violet washes"></div>
      <div class="back-content">
        <p class="tagline">UNIQUE AND AFFORDABLE SKIN CARE JUST FOR <span class="tagline__accent">YOU</span></p>
        <p class="specialty">SPECIALIZING IN VERIDIA SKIN CARE PRODUCTS</p>
        <h2 class="owner">Marisa Holloway</h2>
        <p class="owner-title">LICENSED ESTHETICIAN</p>
        <address class="contact">
          412 Elm Avenue Fairview, CO 80699<br>
          555-014-2730<br>
          glowbloombymarisa.com
        </address>
      </div>
    </section>
  </main>
</body>
</html>
```